Business Card Design

We need a business card designed to portray the message that we are wedding and event stylists. We set up garden ceremonies and style wedding reception venues with chair covers and sashes, backdrops and draping's, wishing wells, tealight holders, table centerpieces. We also style corporate functions - Christmas parties, gala dinners, school formals, award nights. The colour of our uniforms are black and hot pink, if these colours could be incorporated. We would like to be able to use this design for letterhead, flyers and postcards etc. We would like the design to portray a professional, classic image that would relate to both spectrums of our business, weddings and corporate events. If you could develop a logo to incorporate would be great

Target Market(s)

brides, corporate compaines

Industry/Entity Type

Wedding

Contact Information for Business Card

Velvet Crest Occasions & Party Hire
Phone: 0417 553 916 Email:vcoph@fernmail.example
Web: www.velvetcrestoccasions.example.au

Requirements
Must have
• Must include that we set up for weddings, engagements, birthdays, anniversaries, corporate functions, school formals, any occasion.

```html
<!DOCTYPE html>
<html lang="en">
<head>
<meta charset="utf-8">
<title>Velvet Crest Occasions &amp; Party Hire — Business Card</title>
<link rel="stylesheet" href="https://fonts.googleapis.com/css2?family=Cinzel:wght@400;700&display=swap">
<style>
  :root {
    --paper: #ffffff;
    --ink: #000000;
    --hot-pink: #e61ee6;
    --light: #ffffff;
    --services-grey: #1f1f1f;
  }
  html, body {
    margin: 0;
    padding: 0;
    width: 1200px;
    height: 741px;
    overflow: hidden;
    background: var(--paper);
  }
  .card {
    position: relative;
    width: 1200px;
    height: 741px;
    font-family: "Cinzel", "Times New Roman", serif;
  }
  .card__top {
    position: absolute;
    inset: 0 0 auto 0;
    height: 370px;
    background: var(--paper);
  }
  .brand-name {
    position: absolute;
    left: 0;
    right: 0;
    top: 95px;
    margin: 0;
    text-align: center;
    color: var(--hot-pink);
    font-weight: 400;
    line-height: 1.15;
    letter-spacing: 3px;
  }
  .brand-name__main {
    display: block;
    font-size: 70px;
  }
  .brand-name__sub {
    display: block;
    font-size: 52px;
  }
  .card__bottom {
    position: absolute;
    inset: 370px 0 0 0;
    background: var(--ink);
  }
  .services {
    position: absolute;
    left: 0;
    right: 0;
    top: 100px;
    margin: 0;
    padding: 0;
    list-style: none;
    text-align: center;
    color: var(--services-grey);
    font-size: 25px;
    line-height: 47px;
    letter-spacing: 2px;
    text-transform: uppercase;
  }
  .contact {
    position: absolute;
    left: 0;
    right: 0;
    top: 121px;
    text-align: center;
    color: var(--light);
    letter-spacing: 2px;
  }
  .contact p { margin: 0; }
  .contact__person {
    font-size: 26px;
    font-weight: 700;
    line-height: 40px;
  }
  .contact__details {
    font-size: 23px;
    line-height: 50px;
    text-transform: uppercase;
  }
  .contact__phone {
    color: var(--hot-pink);
    font-weight: 700;
  }
  .contact__web {
    font-size: 23px;
    line-height: 44px;
    text-transform: uppercase;
  }
</style>
</head>
<body>
  <main class="card">
    <section class="card__top">
      <h1 class="brand-name">
        <span class="brand-name__main">Velvet Crest Occasions</span>
        <span class="brand-name__sub">&amp; Party Hire</span>
      </h1>
    </section>
    <section class="card__bottom">
      <ul class="services">
        <li>Styling for Weddings | Engagements</li>
        <li>Birthdays | Anniversaries</li>
        <li>Corporate Functions | School Formals | Any Occasion</li>
      </ul>
      <div class="contact">
        <p class="contact__person">Corinne Hale | Stylist</p>
        <p class="contact__details">Phone: <span class="contact__phone">0417 553 916</span> | Email: vcoph@fernmail.example</p>
        <p class="contact__web">www.velvetcrestoccasions.example.au</p>
      </div>
    </section>
  </main>
</body>
</html>
```